Cannabis & Shroom Informative

Online Blog/Informative website design
Example site: https://herbalnookwest.com/

I will need the Ad space as well.

Target Market(s)

Cannabis and (psyho) Mushroom Users

Number of Pages Required

1 page

Colors

```html
<!DOCTYPE html>
<html lang="en">
<head>
<meta charset="utf-8">
<title>Sporeleaf Informative</title>
<link rel="stylesheet" href="https://fonts.googleapis.com/css2?family=Poppins:wght@400;500;600;700;800&display=swap">
<style>
:root{
  --green:#5bab2e;
  --green-dark:#1f4e2c;
  --green-deep:#173d22;
  --ink:#1e1e1e;
  --muted:#6b6b6b;
  --soft:#f2f2f2;
  --white:#ffffff;
}
*{box-sizing:border-box;margin:0;padding:0}
html,body{width:1200px;height:4360px;overflow:hidden}
body{position:relative;background:var(--white);font-family:"Poppins",sans-serif;color:var(--ink)}
.abs{position:absolute}
.brand{display:flex;align-items:center;gap:10px;font-weight:700;color:var(--green);font-size:20px;letter-spacing:.5px}
.brand-dot{width:34px;height:34px;border-radius:50%;background:var(--green)}
.btn{display:inline-block;background:var(--green);color:var(--white);font-size:13px;font-weight:600;padding:14px 30px;border-radius:30px}
.photo{border-radius:2px}
.accent{color:var(--green)}
.section-title{font-size:36px;font-weight:800;text-align:center;text-transform:uppercase;width:1200px;left:0}
.para{font-size:14px;line-height:24px;color:var(--muted)}

/* header */
.topbar{left:600px;top:0;width:600px;height:36px;background:var(--green);color:var(--white);font-size:13px;display:flex;align-items:center;justify-content:flex-end;gap:12px;padding-right:100px;border-bottom-left-radius:18px}
.topbar .soc{width:16px;height:16px;border-radius:50%;background:rgba(255,255,255,.8)}
.logo-head{left:110px;top:38px}
.nav{left:490px;top:54px;display:flex;gap:8px;font-size:14px;font-weight:500}
.nav a{padding:14px 22px;color:var(--ink);text-decoration:none}
.nav a.active{background:var(--green);color:var(--white)}

/* hero */
.hero{left:0;top:120px;width:1200px;height:570px;background:radial-gradient(ellipse at 50% 40%,#d9c7aa 0%,#9a7d5a 55%,#4b3a28 100%)}
.hero-title{left:0;top:340px;width:1200px;text-align:center;color:var(--white);font-size:52px;font-weight:800;letter-spacing:1px}
.arrow{top:370px;width:30px;height:30px}
.card{top:570px;width:320px;height:210px;box-shadow:0 6px 18px rgba(0,0,0,.2);overflow:hidden}
.card .img{position:absolute;inset:0}
.card .cap{position:absolute;left:0;right:0;bottom:0;padding:14px 20px;background:rgba(20,30,20,.55);color:var(--white);font-size:14px;font-weight:600;line-height:20px}
.card.dark{background:#3d4436}
.card.dark .cap{top:40px;bottom:auto;background:none}
.more{display:block;margin-top:10px;font-weight:500;font-size:13px}

/* about */
.about-h{left:110px;top:830px;font-size:36px;font-weight:800;line-height:42px}
.about-p{left:110px;top:930px;width:470px}
.about-frame{left:1060px;top:840px;width:140px;height:360px;background:var(--green)}
.about-photo{left:640px;top:870px;width:460px;height:310px;background:linear-gradient(135deg,#e8f1f6,#9fc0d3 60%,#5d8aa5)}

/* press */
.press{left:0;top:1300px;width:1200px;height:570px;background:var(--soft)}
.press-item{top:1530px;width:320px;height:210px}

/* cannabis band */
.band{left:0;top:1920px;width:1200px;height:380px;background:linear-gradient(90deg,#dfe7d8 0%,#f4f6f1 55%,#fbfbf8 100%)}
.band-photo{left:0;top:1920px;width:620px;height:380px;background:radial-gradient(ellipse at 40% 50%,#7fa35a 0%,#b7c3a6 55%,#e4e8df 100%)}

/* dispensaries */
.disp{top:2460px;width:160px;height:160px;background:var(--white);box-shadow:0 4px 16px rgba(0,0,0,.12);display:flex;align-items:center;justify-content:center}
.disp .badge{width:76px;height:76px;border-radius:50%;background:#dfe9d6;border:3px solid var(--green)}
.disp-cap{top:2640px;width:160px;text-align:center;font-size:13px;font-weight:500}

/* ad */
.ad{left:110px;top:2730px;width:980px;height:220px;background:var(--white);box-shadow:0 4px 16px rgba(0,0,0,.15);overflow:hidden}

/* articles */
.art-img{width:313px;height:200px}
.art-title{width:313px;font-size:16px;font-weight:700;line-height:22px}
.art-date{font-size:12px;color:var(--muted);display:flex;align-items:center;gap:6px}

/* footer */
.footer{left:0;top:3940px;width:1200px;height:420px;background:var(--green-dark);color:#d5e3d3}
.footer h4{font-size:18px;font-weight:600;color:var(--white)}
.fl{list-style:none;font-size:13px;line-height:24px}
.field{border-bottom:1px solid rgba(255,255,255,.35);font-size:12px;padding-bottom:8px;color:#cfe0cc}
.fsoc{width:34px;height:34px;border-radius:50%;background:#3c6a45}
.fsoc.on{background:var(--green)}
.bottom{left:0;top:4300px;width:1200px;height:60px;background:var(--green-deep);color:#b9cbb7;font-size:12px;display:flex;align-items:center;justify-content:flex-end;padding-right:110px}
</style>
</head>
<body>

<!-- header -->
<div class="abs topbar">
  <svg width="16" height="16" viewBox="0 0 24 24"><path d="M6.6 10.8a15 15 0 006.6 6.6l2.2-2.2a1 1 0 011-.25 11 11 0 003.6.6 1 1 0 011 1V20a1 1 0 01-1 1A17 17 0 013 4a1 1 0 011-1h3.5a1 1 0 011 1 11 11 0 00.6 3.6 1 1 0 01-.25 1z" fill="#fff"/></svg>
  <span>Call us Today</span>
  <span class="soc"></span><span class="soc"></span><span class="soc"></span><span class="soc"></span>
  <span style="font-weight:600">+1 999 999 9999</span>
</div>
<div class="abs logo-head brand"><span class="brand-dot"></span>SPORELEAF INFORMATIVE</div>
<nav class="abs nav">
  <a class="active">Home</a><a>About us</a><a>Services</a><a>Blog</a><a>Information</a><a>Contact us</a>
</nav>

<!-- hero -->
<div class="abs hero" role="img" aria-label="Basket of fresh white mushrooms with parsley"></div>
<div class="abs hero-title">SPORELEAF INFORMATIVE</div>
<svg class="abs arrow" style="left:60px" viewBox="0 0 30 30"><path d="M19 6L10 15l9 9" stroke="#fff" stroke-width="3" fill="none"/></svg>
<svg class="abs arrow" style="left:1110px" viewBox="0 0 30 30"><path d="M11 6l9 9-9 9" stroke="#fff" stroke-width="3" fill="none"/></svg>

<div class="abs card" style="left:112px">
  <div class="img" role="img" aria-label="Sliced mushrooms on a board" style="background:linear-gradient(135deg,#e6d6c0,#b08a66)"></div>
  <div class="cap">Lorem ipsum dolor sit amet, conse ctetur adipiscing</div>
</div>
<div class="abs card dark" style="left:440px">
  <div class="cap">Lorem ipsum dolor sit amet, conse ctetur adipiscing<span class="more">More info &gt;</span></div>
</div>
<div class="abs card" style="left:768px">
  <div class="img" role="img" aria-label="White mushrooms on a green cloth" style="background:linear-gradient(135deg,#f1ede4,#c9c0a8 60%,#7ba155)"></div>
  <div class="cap">Lorem ipsum dolor sit amet, conse ctetur adipiscing</div>
</div>

<!-- about -->
<div class="abs about-h">ABOUT<br><span class="accent">SPORELEAF INFORMATIVE</span></div>
<div class="abs about-p para">
  <p>Lorem ipsum dolor sit amet, consectetur adipiscing elit, sed do eiusmod tempor incididunt ut labore et dolore magna aliqua. Ut enim ad minim veniam, quis nostrud exercitation ullamco laboris.</p>
  <p style="margin-top:16px">Duis aute irure dolor in reprehenderit in voluptate velit esse cillum dolore eu fugiat nulla pariatur. Excepteur sint occaecat cupidatat non proident, sunt in culpa qui officia deserunt mollit anim id est laborum.</p>
</div>
<div class="abs" style="left:110px;top:1148px"><span class="btn">READ MORE »</span></div>
<div class="abs about-frame"></div>
<div class="abs about-photo" role="img" aria-label="Scientist in gloves examining a cannabis seedling"></div>

<!-- press -->
<div class="abs press"></div>
<div class="abs section-title" style="top:1395px">Fresh from <span class="accent">the press</span></div>
<div class="abs para" style="left:300px;top:1455px;width:600px;text-align:center">Lorem ipsum dolor sit amet, consectetur adipiscing elit, sed do eiusmod tempor incididunt ut labore et dolore magna aliqua. Ut enim ad minim veniam.</div>
<div class="abs press-item" style="left:110px;background:linear-gradient(135deg,#c9d9b4,#6f8f4d)" role="img" aria-label="Gloved hands holding dried cannabis buds"></div>
<div class="abs press-item" style="left:440px;background:#3f3f3f">
  <div style="position:absolute;left:30px;top:70px;color:#fff;font-size:15px;font-weight:600;line-height:22px">Lorem ipsum dolor sit amet, conse ctetur adipiscing</div>
</div>
<div class="abs press-item" style="left:770px;background:linear-gradient(135deg,#f3c46a,#d6862a)" role="img" aria-label="Golden chanterelle mushrooms"></div>
<div class="abs" style="left:530px;top:1770px"><span class="btn">READ MORE »</span></div>

<!-- cannabis band -->
<div class="abs band"></div>
<div class="abs band-photo" role="img" aria-label="Hands holding a fresh cannabis plant"></div>
<div class="abs" style="left:640px;top:2000px;font-size:36px;font-weight:700">What is <span class="accent">Cannabis?</span></div>
<div class="abs para" style="left:640px;top:2065px;width:460px">Lorem ipsum dolor sit amet, consectetur adipiscing elit, sed do eiusmod tempor incididunt ut labore et dolore magna aliqua. Ut enim ad minim veniam, quis nostrud exercitation ullamco laboris nisi ut aliquip ex ea commodo consequat duis aute irure.</div>

<!-- dispensaries -->
<div class="abs section-title" style="top:2390px">Our top <span class="accent">dispensaries</span></div>
<div class="abs disp" style="left:148px"><span class="badge"></span></div>
<div class="abs disp" style="left:396px"><span class="badge"></span></div>
<div class="abs disp" style="left:640px"><span class="badge"></span></div>
<div class="abs disp" style="left:884px"><span class="badge"></span></div>
<div class="abs disp-cap" style="left:148px">Lorem ipsum dolor</div>
<div class="abs disp-cap" style="left:396px">Lorem ipsum dolor</div>
<div class="abs disp-cap" style="left:640px">Lorem ipsum dolor</div>
<div class="abs disp-cap" style="left:884px">Lorem ipsum dolor</div>

<!-- ad -->
<div class="abs ad">
  <svg style="position:absolute;left:0;top:0" width="420" height="220"><path d="M0 0H400L340 220H0Z" fill="#1f4e2c"/></svg>
  <div style="position:absolute;left:34px;top:36px;color:#fff">
    <div style="font-size:26px;font-weight:700;line-height:30px">Lorem ipsum dolor</div>
    <div style="font-size:14px;margin-top:6px">sit amet, consectetur adipiscing</div>
    <div style="font-size:13px;margin-top:22px;display:flex;align-items:center;gap:10px">Use Coupon Code : <span style="background:var(--green);padding:8px 16px;font-weight:600">SITE5</span></div>
  </div>
  <div class="brand" style="position:absolute;left:380px;top:92px;font-size:18px"><span class="brand-dot"></span>SPORELEAF INFORMATIVE</div>
  <div role="img" aria-label="Cannabis leaves" style="position:absolute;left:680px;top:30px;width:180px;height:160px;background:radial-gradient(circle,#5f9a3a,#a9c98d 60%,rgba(255,255,255,0))"></div>
  <div style="position:absolute;left:840px;top:-10px;width:240px;height:240px;border-radius:50%;background:var(--green)"></div>
  <div style="position:absolute;left:860px;top:60px;width:110px;text-align:center;color:#fff;font-size:32px;font-weight:800;line-height:38px">50%<br>Off</div>
</div>
<div class="abs" role="img" aria-label="Brown mushrooms" style="left:950px;top:2880px;width:250px;height:130px;border-radius:50% 50% 10px 10px;background:radial-gradient(ellipse at 50% 30%,#c7a27a,#7a5534)"></div>

<!-- articles -->
<div class="abs section-title" style="top:3090px">Latest <span class="accent">articles</span></div>

<div class="abs art-img" style="left:110px;top:3170px;background:linear-gradient(135deg,#c79e73,#6e4c2f)" role="img" aria-label="Pile of brown mushrooms"></div>
<div class="abs art-img" style="left:443px;top:3170px;background:linear-gradient(135deg,#d9e2cf,#6e8a57)" role="img" aria-label="Jars of cannabis buds"></div>
<div class="abs art-img" style="left:776px;top:3170px;background:linear-gradient(135deg,#8a6a45,#3f2e1c)" role="img" aria-label="Wild mushrooms in a forest"></div>
<div class="abs art-title" style="left:110px;top:3388px">Lorem ipsum dolor sit amet, conse ctetur adipiscing</div>
<div class="abs art-title" style="left:443px;top:3388px">Lorem ipsum dolor sit amet, conse ctetur adipiscing</div>
<div class="abs art-title" style="left:776px;top:3388px">Lorem ipsum dolor sit amet, conse ctetur adipiscing</div>
<div class="abs art-date" style="left:110px;top:3444px"><svg width="12" height="12"><rect x="1" y="2" width="10" height="9" fill="none" stroke="#888"/></svg>05 Jan 2022</div>
<div class="abs art-date" style="left:443px;top:3444px"><svg width="12" height="12"><rect x="1" y="2" width="10" height="9" fill="none" stroke="#888"/></svg>05 Jan 2022</div>
<div class="abs art-date" style="left:776px;top:3444px"><svg width="12" height="12"><rect x="1" y="2" width="10" height="9" fill="none" stroke="#888"/></svg>05 Jan 2022</div>

<div class="abs art-img" style="left:110px;top:3490px;background:linear-gradient(135deg,#a9b98f,#4e6b36)" role="img" aria-label="Hands trimming a cannabis plant"></div>
<div class="abs art-img" style="left:443px;top:3490px;background:linear-gradient(135deg,#b8916b,#5b3d26)" role="img" aria-label="Shiitake mushrooms on a tray"></div>
<div class="abs art-img" style="left:776px;top:3490px;background:linear-gradient(135deg,#9fc382,#3f6a2c)" role="img" aria-label="Rows of cannabis plants in a greenhouse"></div>
<div class="abs art-title" style="left:110px;top:3708px">Lorem ipsum dolor sit amet, conse ctetur adipiscing</div>
<div class="abs art-title" style="left:443px;top:3708px">Lorem ipsum dolor sit amet, conse ctetur adipiscing</div>
<div class="abs art-title" style="left:776px;top:3708px">Lorem ipsum dolor sit amet, conse ctetur adipiscing</div>
<div class="abs art-date" style="left:110px;top:3764px"><svg width="12" height="12"><rect x="1" y="2" width="10" height="9" fill="none" stroke="#888"/></svg>05 Jan 2022</div>
<div class="abs art-date" style="left:443px;top:3764px"><svg width="12" height="12"><rect x="1" y="2" width="10" height="9" fill="none" stroke="#888"/></svg>05 Jan 2022</div>
<div class="abs art-date" style="left:776px;top:3764px"><svg width="12" height="12"><rect x="1" y="2" width="10" height="9" fill="none" stroke="#888"/></svg>05 Jan 2022</div>

<div class="abs" style="left:520px;top:3840px"><span class="btn">MORE ARTICLES »</span></div>

<!-- footer -->
<footer class="abs footer">
  <div class="brand" style="position:absolute;left:110px;top:50px;font-size:18px"><span class="brand-dot"></span>SPORELEAF INFORMATIVE</div>
  <p style="position:absolute;left:110px;top:110px;width:300px;font-size:13px;line-height:22px">Lorem ipsum dolor sit amet, consectetur adipiscing elit, sed do eiusmod tempor incididunt ut labore et dolore magna aliqua. Ut enim ad minim veniam, quis nostrud exercitation.</p>
  <div style="position:absolute;left:110px;top:290px;display:flex;gap:12px"><span class="fsoc"></span><span class="fsoc on"></span><span class="fsoc"></span><span class="fsoc"></span></div>

  <h4 style="position:absolute;left:480px;top:60px">Quick Links</h4>
  <ul class="fl" style="position:absolute;left:480px;top:100px"><li>Home</li><li>About us</li><li>Services</li><li>Blog</li><li>Information</li><li>Contact us</li></ul>

  <h4 style="position:absolute;left:720px;top:60px">Contact us</h4>
  <div class="field" style="position:absolute;left:720px;top:110px;width:170px">First name*</div>
  <div class="field" style="position:absolute;left:910px;top:110px;width:180px">Last name*</div>
  <div class="field" style="position:absolute;left:720px;top:160px;width:170px">Phone*</div>
  <div class="field" style="position:absolute;left:910px;top:160px;width:180px">Email Address*</div>
  <div class="field" style="position:absolute;left:720px;top:215px;width:370px;height:60px">Message*</div>
  <svg style="position:absolute;left:1066px;top:240px" width="20" height="20" viewBox="0 0 24 24"><path d="M2 21l21-9L2 3v7l15 2-15 2z" fill="#fff"/></svg>
</footer>
<div class="abs bottom">© 2022 Sporeleaf Informative. All rights reserved&nbsp;&nbsp;Privacy&nbsp;&nbsp;Terms of Use&nbsp;&nbsp;Cookies</div>

</body>
</html>
```